Update Letterhead for Harbor Lane Advisors

We need a modernized and updated letterhea. We DO NOT want to change fonts, we want incorporate the logo and words better and make a sleeker and elegant logo catering to wealthy clients. Harbor is a wealth management firm catering to business owners, physicians, and high net wort clientele. Our letterhead should have strength and elegance and cater to that market. Guaranteed payment.

Requirements
Must have
• PLEASE NOTE THAT THE LOGO USED IN THE ORIGINAL DESIGNS ARE INCORRECT! Please update to the new logo!
• We also changed our color scheme to grey and gold and black. Please refer to website www.harborla-example.com to see what I mean as we want to update to that rather than the dark blue. (Most likely grey and gold)

```html
<!DOCTYPE html>
<html lang="en">
<head>
<meta charset="utf-8">
<title>Harbor Lane Advisors — Letterhead</title>
<link href="https://fonts.googleapis.com/css2?family=Arimo:wght@400;700&family=Didact+Gothic&display=swap" rel="stylesheet">
<style>
  :root {
    --backdrop: #e6e6e6;
    --paper: #f5f5f5;
    --paper-shade: #ececec;
    --gold: #c9a961;
    --ink: #3f3f3f;
    --ink-soft: #555555;
    --rule-grey: #8a8a8a;
    --signature-tone: #d7dff0;
    --badge-tone: #b9b9b9;
  }
  * { box-sizing: border-box; margin: 0; padding: 0; }
  html, body { width: 1024px; height: 1200px; overflow: hidden; }
  body { background: var(--backdrop); position: relative; font-family: "Arimo", Arial, sans-serif; }

  .letterhead {
    position: absolute; left: 101px; top: 25px; width: 822px; height: 1150px;
    background: linear-gradient(100deg, var(--paper) 0%, #f0f0f0 60%, var(--paper-shade) 100%);
    box-shadow: 0 2px 10px rgba(0,0,0,.12);
    color: var(--ink);
  }

  .sender { position: absolute; left: 74px; top: 78px; font-size: 11px; line-height: 15px; color: var(--ink-soft); }
  .sender-name { color: var(--gold); font-weight: 700; font-size: 15px; line-height: 17px; }
  .sender-title { font-size: 13px; line-height: 16px; color: var(--ink); letter-spacing: .2px; margin-bottom: 10px; }
  .contact-line { display: flex; align-items: center; gap: 6px; }
  .contact-line svg { width: 10px; height: 10px; fill: var(--gold); }
  .office { margin-top: 9px; }
  .office-label { color: var(--gold); font-weight: 700; font-size: 10.5px; }

  .brand-band { position: absolute; left: 613px; top: 0; width: 69px; height: 118px; }
  .brand { position: absolute; left: 540px; top: 168px; width: 230px; text-align: center; color: var(--gold); font-weight: 700; }
  .brand-name { font-size: 22px; letter-spacing: 1px; line-height: 24px; }
  .brand-rule { height: 2px; background: var(--rule-grey); margin: 4px 0 3px; }
  .brand-sub { font-size: 11px; letter-spacing: 2px; text-align: right; }

  .letter-body { position: absolute; left: 74px; top: 340px; width: 679px; font-family: "Didact Gothic", "Century Gothic", sans-serif; }
  .salutation { font-size: 20px; color: var(--ink); margin-bottom: 30px; }
  .letter-body p.paragraph { font-size: 11.3px; line-height: 15.4px; text-align: justify; color: var(--ink-soft); margin-bottom: 15px; }
  .closing { font-size: 11.3px; color: var(--ink-soft); margin-top: 30px; }
  .signature { display: block; width: 140px; height: 66px; margin-top: 34px; background: var(--signature-tone); border-radius: 4px; }

  .memberships { position: absolute; left: 276px; top: 942px; width: 272px; height: 56px; display: flex; justify-content: space-between; align-items: center; padding: 0 6px; }
  .membership-badge { background: var(--badge-tone); }
  .badge-circle { width: 56px; height: 44px; border-radius: 50% 50% 6px 6px; }
  .badge-triangle { width: 54px; height: 48px; clip-path: polygon(50% 0, 100% 100%, 0 100%); }
  .badge-round { width: 38px; height: 38px; border-radius: 50%; }
  .badge-tall { width: 22px; height: 52px; border-radius: 3px; }

  .mission { position: absolute; left: 74px; top: 1007px; width: 672px; text-align: center; }
  .mission-heading { display: flex; align-items: center; gap: 6px; color: var(--gold); font-weight: 700; font-size: 11px; }
  .mission-heading::before, .mission-heading::after { content: ""; flex: 1; height: 1px; background: var(--gold); }
  .mission-text { font-size: 11.2px; line-height: 14px; color: var(--ink); letter-spacing: .3px; margin-top: 1px; }
  .mission-rule { height: 1px; background: var(--gold); margin: 7px 0 6px; }
  .disclosure { font-size: 7.3px; line-height: 10.5px; color: var(--ink-soft); padding: 0 6px; }
</style>
</head>
<body>
  <main class="letterhead">
    <header class="sender">
      <div class="sender-name">Margaret Lowell Hayes, CFP , MSFS, AEP</div>
      <div class="sender-title">PRESIDENT &amp; FINANCIAL ADVISOR</div>
      <div class="contact-line"><svg viewBox="0 0 10 10"><path d="M2 0.5 L3.8 2.6 L2.8 3.8 Q4 6.2 6.2 7.2 L7.4 6.2 L9.5 8 L8.2 9.5 Q2.5 8.5 0.5 1.8 Z"/></svg>555.010.4300</div>
      <div class="contact-line"><svg viewBox="0 0 10 10"><path d="M0.5 2 H9.5 V8 H0.5 Z M0.5 2 L5 5.5 L9.5 2" fill="none" stroke="#c9a961" stroke-width="1.2"/></svg>mhayes@harborla-example.com</div>
      <div class="contact-line"><svg viewBox="0 0 10 10"><circle cx="5" cy="5" r="4.5"/><path d="M0.5 5 H9.5 M5 0.5 V9.5" stroke="#f5f5f5" stroke-width="0.9"/></svg>www.harborla-example.com</div>
      <div class="office">
        <div class="office-label">DOWNTOWN OFFICE</div>
        <div>210 Bayview Street, Suite 1100</div>
        <div>Harborton, TX 70001</div>
      </div>
      <div class="office">
        <div class="office-label">WESTSIDE OFFICE</div>
        <div>4800 Meridian Drive, Suite A</div>
        <div>Harborton, TX 70022</div>
      </div>
    </header>

    <svg class="brand-band" viewBox="0 0 69 118" aria-hidden="true">
      <rect x="0" y="0" width="69" height="80" fill="#c9a961"/>
      <circle cx="34.5" cy="80" r="37" fill="#c9a961"/>
    </svg>
    <div class="brand">
      <div class="brand-name">HARBOR LANE</div>
      <div class="brand-rule"></div>
      <div class="brand-sub">ADVISORS</div>
    </div>

    <section class="letter-body">
      <p class="salutation">Dear Mr. Carter,</p>
      <p class="paragraph">Lorem ipsum dolor sit amet, consectetur adipiscing elit. Donec orci purus, luctus vitae dignissim eu, iaculis sed purus. Vivamus faucibus, ipsum nec aliquet viverra, leo mauris condimentum ligula, sit amet sagittis enim ligula quis arcu. Nam egestas tortor id nisi porttitor mattis. In tortor ante, ultricies in suscipit a, tempus non massa. Vivamus et auctor mi. Fusce vel massa nulla. Phasellus nec eros mauris, et scelerisque orci.</p>
      <p class="paragraph">Donec malesuada orci vitae nulla accumsan porta a id massa. Quisque accumsan iaculis magna sit amet fringilla. Maecenas consequat, magna eget tincidunt semper, odio nibh rutrum mi, id feugiat ante nisi eu risus. Vestibulum nunc orci, rhoncus a placerat in, ultricies in mi. Cras mattis varius eros, vel fringilla nisi suscipit eget. Quisque scelerisque sagittis nulla at porttitor.</p>
      <p class="paragraph">Sed id augue vitae urna euismod commodo aliquet a quam. Pellentesque arcu velit, cursus et malesuada ut, consequat et diam. Nullam erat sem, rhoncus id ullamcorper vitae, rhoncus et arcu. In ultricies ultricies nulla, ut rutrum nisi iaculis at. Donec eu magna a metus ornare faucibus. Fusce aliquet faucibus ultricies. Morbi semper, est id tincidunt gravida, sem arcu adipiscing lacus, ac bibendum nulla leo eu purus. Quisque nec diam sed risus consectetur a ccumsan quis quis nibh. Vestibulum id purus lorem.</p>
      <p class="paragraph">It is a long established fact that a reader will be distracted by the readable content of a page when looking at its layout. The point of using Lorem Ipsum is that it has a more-or-less normal distribution of letters, as opposed to using 'Content here, content here', making it look like readable English. Many desktop publishing packages</p>
      <p class="closing">Sincerely,</p>
      <span class="signature" role="img" aria-label="Handwritten blue ink signature of James Porter"></span>
    </section>

    <div class="memberships" aria-label="Professional memberships">
      <span class="membership-badge badge-circle"></span>
      <span class="membership-badge badge-triangle"></span>
      <span class="membership-badge badge-round"></span>
      <span class="membership-badge badge-tall"></span>
    </div>

    <footer class="mission">
      <div class="mission-heading">OUR MISSION STATEMENT</div>
      <p class="mission-text">"WE EMPOWER OUR CLIENTS TO REALIZE FINANCIAL INDEPENDENCE BY SECURING<br>TODAY, TOMORROW AND THE FUTURE. ONE FAMILY, ONE SOLUTION, AND ONE LEGACY AT A TIME."</p>
      <div class="mission-rule"></div>
      <p class="disclosure">*Margaret Lowell Hayes, CFP , a Financial Adviser offering investment advisory services through Bayline Advisory Group LLC, a Registered Investment Adviser. Registered Representative offering securities through Northgate Securities LLC, Member of the industry regulator, a Licensed Insurance Agency, 210 Bayview Street, Suite 1100, Harborton, TX 70001. 555-010-3200. Member Agent, Seaward Planning Network, a service of Northgate Life Company. Harbor Lane Advisors is not owned or operated by Northgate Securities LLC or its affiliates.</p>
    </footer>
  </main>
</body>
</html>
```